Newsletter Header - Insert Cutting Branch

We have a Hollis Grant Foundation (HGF) Logo (see attached) and are creating a Newsletter with the title: The Green Ledger. The founders of the HGF were nursery people and started their plants via cuttings. So, we want to take a branch from the HGF logo tree and attach it somewhere in the Newsletter title. You can leave the logo as it is - just want a cutting somewhere in the title. The Green Ledger title should be 3-D
Updates

Target Market(s)

Donors to our Foundation

Industry/Entity Type

Non Profit

Colors

Designer to choose colors to be used in the design.

Requirements
Must have
• Logo remain as is - just a branch duplicate on the header.
Nice to have
• The Green Ledger would be nice to have as a 3-D image

```html
<!DOCTYPE html>
<html lang="en">
<head>
<meta charset="utf-8">
<title>The Green Ledger – Newsletter Header Options</title>
<link href="https://fonts.googleapis.com/css2?family=Rye&family=Big+Shoulders+Display:wght@500&display=swap" rel="stylesheet">
<style>
  :root {
    --canvas: #e0e0e0;
    --white: #ffffff;
    --leaf: #1f9a45;
    --leaf-dark: #176b33;
    --leaf-deep: #2f6a45;
    --leaf-light: #8fd89e;
    --overlay: rgba(31, 154, 69, 0.92);
    --mint-line: #cfe8d6;
    --ink: #444444;
    --pot-red: #b3141d;
    --soil: #3a3330;
  }
  * { margin: 0; padding: 0; box-sizing: border-box; }
  html, body { width: 880px; height: 1200px; overflow: hidden; background: var(--canvas); }
  .canvas { position: relative; width: 880px; height: 1200px; }

  .header-option { position: absolute; overflow: hidden; }
  .photo { position: absolute; inset: 0; }

  .brand-mark {
    display: flex; align-items: center; justify-content: center;
    border-radius: 50%;
    font-family: "Rye", serif;
    font-size: 15px;
    letter-spacing: 1px;
  }

  .title {
    position: relative;
    font-family: "Rye", serif;
    white-space: nowrap;
    text-transform: uppercase;
    line-height: 1;
  }

  /* Branch cutting attached to the title */
  .cutting {
    position: absolute;
    right: -13px;
    top: -12px;
    width: 15px;
    height: 22px;
    border-radius: 80% 0 80% 0;
    transform: rotate(20deg);
    background: linear-gradient(160deg, var(--leaf-light), var(--leaf));
  }
  .on-light .cutting { background: linear-gradient(160deg, var(--leaf), var(--leaf-dark)); }

  /* Option 1 */
  .option-split { left: 170px; top: 153px; width: 542px; height: 176px; }
  .option-split .logo-panel { position: absolute; left: 0; top: 0; width: 132px; height: 176px; background: var(--white); }
  .option-split .frame-line { position: absolute; left: 66px; top: 34px; width: 66px; height: 123px; border: 2px solid var(--mint-line); border-right: none; }
  .option-split .brand-mark { position: absolute; left: 31px; top: 51px; width: 78px; height: 78px; border: 3px solid var(--ink); color: var(--leaf-dark); background: var(--white); }
  .option-split .photo { left: 132px; background: linear-gradient(135deg, #3f9a5a 0%, #2e8647 50%, #3a9353 100%); }
  .option-split .title { position: absolute; left: 159px; top: 94px; transform: translateY(-50%); font-size: 31.5px; color: var(--white); text-shadow: 1px 1px 0 var(--leaf-dark), 2px 2px 0 var(--leaf-dark); }

  /* Option 2 */
  .option-band { left: 170px; top: 363px; width: 542px; height: 163px; }
  .option-band .photo { background: linear-gradient(120deg, #4b8a5c 0%, #2f6a45 45%, #5d9a6d 100%); }
  .option-band .band { position: absolute; left: 45px; top: 37px; width: 450px; height: 95px; background: rgba(255,255,255,0.92); }
  .option-band .brand-mark { position: absolute; left: 19px; top: 20px; width: 56px; height: 56px; border: 3px solid var(--ink); color: var(--leaf-dark); font-size: 12px; }
  .option-band .title { position: absolute; left: 89px; top: 48px; transform: translateY(-50%); font-size: 31.5px; color: var(--leaf); text-shadow: 1px 1px 0 var(--leaf-dark); }

  /* Option 3 */
  .option-pots { left: 167px; top: 582px; width: 545px; height: 182px; }
  .option-pots .photo { background: linear-gradient(90deg, var(--pot-red) 0%, var(--soil) 22%, #5a2a26 55%, var(--soil) 80%, var(--pot-red) 100%); }
  .option-pots .panel { position: absolute; left: 71px; top: 27px; width: 404px; height: 155px; background: var(--leaf); display: flex; flex-direction: column; align-items: center; }
  .option-pots .brand-mark { margin-top: 23px; width: 55px; height: 55px; border: 3px solid var(--white); color: var(--white); font-size: 12px; }
  .option-pots .title { margin-top: 13px; font-size: 31.5px; color: var(--white); text-shadow: 1px 1px 0 var(--leaf-dark), 2px 2px 0 var(--leaf-dark); }

  /* Option 4 */
  .option-garden { left: 167px; top: 818px; width: 545px; height: 182px; }
  .option-garden .photo { background: linear-gradient(90deg, #0d1a12 0%, #2f5a38 16%, #3e7a49 50%, #8fa7a0 84%, #b3c4c0 100%); }
  .option-garden .panel { position: absolute; left: 83px; top: 0; width: 381px; height: 182px; background: var(--overlay); display: flex; flex-direction: column; align-items: center; }
  .option-garden .brand-mark { margin-top: 33px; width: 55px; height: 55px; border: 3px solid var(--white); color: var(--white); font-size: 12px; }
  .option-garden .title { margin-top: 14px; font-family: "Big Shoulders Display", sans-serif; font-weight: 500; font-size: 46px; letter-spacing: 1px; color: var(--white); }
</style>
</head>
<body>
<main class="canvas">

  <section class="header-option option-split">
    <div class="logo-panel">
      <div class="frame-line"></div>
      <div class="brand-mark">HGF</div>
    </div>
    <div class="photo" role="img" aria-label="Rows of potted succulents seen from above under a green tint"></div>
    <h1 class="title">The Green Ledger<span class="cutting" role="img" aria-label="Leafy branch cutting from the foundation tree attached to the title"></span></h1>
  </section>

  <section class="header-option option-band">
    <div class="photo" role="img" aria-label="Potted succulent seedlings in a nursery under a green tint"></div>
    <div class="band on-light">
      <div class="brand-mark">HGF</div>
      <h1 class="title">The Green Ledger<span class="cutting" role="img" aria-label="Leafy branch cutting from the foundation tree attached to the title"></span></h1>
    </div>
  </section>

  <section class="header-option option-pots">
    <div class="photo" role="img" aria-label="Succulent cuttings rooting in red nursery pots"></div>
    <div class="panel">
      <div class="brand-mark">HGF</div>
      <h1 class="title">The Green Ledger<span class="cutting" role="img" aria-label="Leafy branch cutting from the foundation tree attached to the title"></span></h1>
    </div>
  </section>

  <section class="header-option option-garden">
    <div class="photo" role="img" aria-label="Garden beds of young plants beside a stone paved path"></div>
    <div class="panel">
      <div class="brand-mark">HGF</div>
      <h1 class="title">The Green Ledger<span class="cutting" role="img" aria-label="Leafy branch cutting from the foundation tree attached to the title"></span></h1>
    </div>
  </section>

</main>
</body>
</html>
```